Office brochure for chronic pain doctor

I need an brochure for my office, and since I want to be able to mail the brochure, I think trifold would be the best size. I treat patients with chronic head and neck pain, as well as sleep apnea. I treat all of the following:

1. headaches
2. myofascial pain, which is a fancy way of saying muscle pain
3. neuropathic pain, which is a fancy way of saying nerve pain
4. TMJ, which stands for the temporomandibular joint (jaw joint)
5. obstructive sleep apnea

The colors will be based on my logo on my website, which you can see at www.BrightJPR.net, and you can learn more about what I do at my website. JPR stands for orofacial pain, which is a speciality training within the field of dentistry but I do not treat teeth. I have high resolution graphics for the brochure so I need someone with an artistic eye to design and lay out the brochure.

The logo colors are:
Purple 9e80bb
Pink f6b1d0
Blue 0f4b8f
Updates

I had a request for the logo in a .ai or .pdf format, which I have just uploaded. Please let me know if you have any other requests. Thank you, Dale

Target Market(s)

80% female, 20% male. I am in an upscale area of Los Angeles called Beverly Hills but I will see a patient from any area around Los Angeles or from any area in the world.

Industry/Entity Type

Training

Colors
6b449b
e567a6
0355a3

Requirements
Must have
• I want a small section of the brochure to feature each of the five areas I treat, and I have included an image to place in each of the five sections. A small section should include a short bio of me, which you can condense from www.brightjpr.net/dale. The brochure must appeal to women since 80% of my patients are female but I don't want to completely ignore men. Most of the pain patients are female, and most of the sleep apnea patients are male.

Here are the colors in my logo
Purple 9e80bb
Pink f6b1d0
Blue 0f4b8f
Should not have
• Anything related to teeth or dentistry.
No decorative or script fonts.

```html
<!DOCTYPE html>
<html lang="en">
<head>
<meta charset="utf-8">
<title>BrightJPR Trifold Brochure</title>
<link href="https://fonts.googleapis.com/css2?family=Cinzel:wght@600&family=Questrial&family=Arimo:wght@700&display=swap" rel="stylesheet">
<style>
:root{
  --blue:#0f4b8f;
  --purple:#9e80bb;
  --pink:#f6b1d0;
  --ink:#4a4a4a;
  --paper:#f7f7f8;
  --white:#ffffff;
}
*{margin:0;padding:0;box-sizing:border-box}
html,body{width:1200px;height:930px;overflow:hidden;background:#e9e9ec}
.brochure{position:relative;width:1200px;height:930px;background:linear-gradient(180deg,#ececef 0%,var(--white) 40%,var(--paper) 100%);font-family:'Questrial',sans-serif;color:var(--ink)}
.shapes{position:absolute;left:0;top:0}
.fold{position:absolute;top:0;width:1px;height:930px;background:rgba(0,0,0,.08)}
.abs{position:absolute}
.serif-caps{font-family:'Cinzel',serif;font-weight:600}
.bold{font-family:'Arimo',sans-serif;font-weight:700}
.photo{position:absolute;border-radius:10px;box-shadow:0 2px 6px rgba(0,0,0,.25)}

.meet-title{left:32px;top:56px;font-size:23px;color:var(--white);letter-spacing:.5px}
.doctor-photo{left:78px;top:111px;width:240px;height:267px;background:linear-gradient(180deg,#4a5a5a 0%,#6d7a78 55%,#e8eef3 56%,#dfe6ee 100%)}
.bio-name{left:32px;top:393px;font-size:20px;color:var(--blue)}
.bio{left:32px;top:422px;width:331px;font-size:11.6px;line-height:14.6px;text-align:justify}
.bio p{margin-bottom:14px}
.band-phone{left:0;top:860px;width:400px;text-align:center;font-size:24px;color:var(--blue)}

.headline{left:400px;top:78px;width:400px;text-align:center;font-size:21.5px;line-height:29px;color:var(--blue)}
.caring{left:420px;top:168px;width:330px;text-align:right;font-size:31px;line-height:37px;color:var(--white)}
.couple-photo{left:432px;top:324px;width:345px;height:231px;background:linear-gradient(135deg,#f4f1f2 0%,#e6dcd8 50%,#f8f6f6 100%)}
.brand-mark{display:flex;align-items:center;gap:8px;font-size:22px;color:var(--blue)}
.brand-mark .sq{width:18px;height:18px;background:var(--purple)}
.mid-brand{left:421px;top:604px}
.contact{left:429px;top:653px;font-size:13.5px;line-height:16px;color:var(--blue)}
.contact .row{display:flex;gap:5px;align-items:flex-start}
.contact .ic{width:12px;flex:none;margin-top:2px}
.contact .phone{font-size:15px;margin-top:8px}
.contact .fax{margin-top:8px}
.map{left:603px;top:659px;width:165px;height:144px;background:linear-gradient(135deg,#ecebe6 0%,#dcdcd6 100%);border-radius:8px;box-shadow:0 1px 4px rgba(0,0,0,.25)}
.social{left:410px;top:808px;display:flex;gap:6px}
.social span{width:35px;height:35px;border-radius:50%;display:flex;align-items:center;justify-content:center;font-size:10px;color:var(--white)}
.email{left:445px;top:870px;font-size:13.5px;color:var(--blue);display:flex;gap:5px;align-items:center}
.foot-brand{left:640px;top:856px;width:170px;justify-content:center;color:var(--white)}
.foot-brand .sq{background:var(--white)}

.top-brand{left:835px;top:80px;width:322px;justify-content:center;font-size:34px}
.top-brand .sq{width:28px;height:28px}
.pain-photo{width:175px;height:174px}
.p1{left:813px;top:196px;background:linear-gradient(135deg,#e9d9cc,#f5ede7)}
.p2{left:999px;top:196px;background:linear-gradient(135deg,#f2f2f2,#d8c3b4)}
.p3{left:813px;top:375px;background:linear-gradient(135deg,#f0ece6,#8fae4a)}
.p4{left:999px;top:375px;background:linear-gradient(135deg,#f4f2f0,#c9a996)}
.conditions{left:814px;top:595px;list-style:none}
.conditions li{display:flex;align-items:center;gap:8px;height:45.5px;font-size:23.5px;color:var(--blue)}
.web{left:800px;top:865px;width:400px;text-align:center;font-size:17px;letter-spacing:2.5px;color:var(--white);display:flex;justify-content:center;gap:8px;align-items:center}
</style>
</head>
<body>
<main class="brochure">
  <svg class="shapes" width="1200" height="930" viewBox="0 0 1200 930" aria-hidden="true">
    <path d="M0 48 L350 48 Q360 48 366 56 L373 91 L0 91 Z" fill="var(--blue)"/>
    <rect x="411" y="280" width="389" height="282" rx="10" fill="var(--purple)"/>
    <path d="M786 185 Q786 177 794 177 L1200 177 L1200 505 L1140 562 L794 562 Q786 562 786 554 Z" fill="var(--purple)"/>
    <path d="M411 218 L470 152 L780 152 Q791 152 791 164 L791 290 Q791 298 782 298 L419 298 Q411 298 411 290 Z" fill="var(--blue)"/>
    <path d="M0 857 L622 857 L598 902 L0 902 Z" fill="var(--pink)"/>
    <path d="M598 902 L630 844 Q634 837 643 837 L1200 837 L1200 902 Z" fill="var(--purple)"/>
  </svg>
  <div class="fold" style="left:400px"></div>
  <div class="fold" style="left:800px"></div>

  <!-- Panel: about the doctor -->
  <h2 class="abs serif-caps meet-title">Meet Dr. Marlowe</h2>
  <div class="photo doctor-photo" role="img" aria-label="Portrait of Dr. Dale Marlowe in a white coat"></div>
  <h3 class="abs serif-caps bio-name">Dale Marlowe, DDS, MBA</h3>
  <div class="abs bio">
    <p>I have lived in Beverly Hills since 1993, I wanted to practice locally, and was fortunate to find a great location at the corner of Linden Court and Alder Drive, in the Garden Crescent building, which is where Casa Lumen, the restaurant owned by Nora Castellane, is located. It is a great building, and I have tried to create a unique office to help patients suffering from chronic head and neck pain. If you are suffering from migraine headaches, cluster headaches, morning headaches, head and neck muscle pain, sharp shooting electrical type of pain in your head or neck, TMJ (or what you have been told is TMJ), or snoring and/or obstructive sleep apnea, please make an appointment at my Beverly Hills chronic pain office for me to examine you to see if I can help manage or eliminate your pain. I promise, I will not even consider drilling your teeth or intentionally try to change your bite to help reduce your pain!</p>
    <p>If you are a dentist, and are interesting in hearing me speak, please know that I have presented at small study clubs, local dental societies, and annual state dental association meetings, and from groups as small as 20 to an audience as large as 2,000. Here are some good testimonials to read from other dentists so please let me know if you are interested in hearing me speak. I guarantee that I will make you think!</p>
    <p>And, yes, I still ride my bike. That is something I don't want to change.</p>
  </div>
  <div class="abs bold band-phone">
    <svg width="26" height="26" viewBox="0 0 26 26" style="vertical-align:-5px"><circle cx="13" cy="13" r="11.5" fill="none" stroke="var(--purple)" stroke-width="1.5"/><path d="M9 7 L12 10 L10.5 12 Q12 15 14 15.5 L16 14 L19 17 L17 19 Q10 19 7 9 Z" fill="var(--purple)"/></svg>
    (888) 555-0142
  </div>

  <!-- Panel: cover -->
  <h1 class="abs headline">Dr. Dale Marlowe<br>Beverly Hills Facial Pain Doctor</h1>
  <div class="abs serif-caps caring">Caring for<br>Head Pain and<br>Sleep Apnea</div>
  <div class="photo couple-photo" role="img" aria-label="Woman covering her ears beside a snoring man in bed"></div>
  <div class="abs brand-mark mid-brand"><span class="sq"></span>BrightJPR</div>
  <div class="abs contact">
    <div class="row"><svg class="ic" viewBox="0 0 12 16"><path d="M6 1 A4.5 4.5 0 0 1 10.5 5.5 Q10.5 9 6 15 Q1.5 9 1.5 5.5 A4.5 4.5 0 0 1 6 1 Z" fill="none" stroke="var(--purple)" stroke-width="1.6"/></svg><div>4820 Linden Court<br>Suite 210<br>Beverly Hills,<br>California 90210</div></div>
    <div class="row phone bold"><svg class="ic" viewBox="0 0 12 12"><circle cx="6" cy="6" r="5.3" fill="none" stroke="var(--purple)"/></svg>(888) 555-0142</div>
    <div class="row fax"><svg class="ic" viewBox="0 0 12 12"><rect x="1" y="5" width="10" height="6" fill="none" stroke="var(--purple)"/><rect x="3" y="1" width="6" height="4" fill="none" stroke="var(--purple)"/></svg>(310) 555-0178</div>
    <div class="row"><svg class="ic" viewBox="0 0 12 12"><circle cx="6" cy="6" r="5" fill="none" stroke="var(--purple)"/><path d="M1 6 H11 M6 1 V11" stroke="var(--purple)"/></svg>www.BrightJPR.net</div>
  </div>
  <div class="abs map" role="img" aria-label="Street map showing the office location in Beverly Hills"></div>
  <div class="abs social">
    <span style="background:#2c8fd6">Flit</span>
    <span style="background:#d7342b">Reel</span>
    <span style="background:#d7342b">Circl</span>
    <span style="background:#f28a24">Jot</span>
    <span style="background:#c8202a">Rate</span>
  </div>
  <div class="abs email"><svg width="13" height="10" viewBox="0 0 13 10"><rect x=".5" y=".5" width="12" height="9" fill="none" stroke="var(--purple)"/><path d="M.5 .5 L6.5 6 L12.5 .5" fill="none" stroke="var(--purple)"/></svg>relief@brightjpr.net</div>
  <div class="abs brand-mark foot-brand"><span class="sq"></span>BrightJPR</div>

  <!-- Panel: conditions -->
  <div class="abs brand-mark top-brand"><span class="sq"></span>BrightJPR</div>
  <div class="photo pain-photo p1" role="img" aria-label="Woman holding her temples with a headache"></div>
  <div class="photo pain-photo p2" role="img" aria-label="Woman rubbing a painful neck"></div>
  <div class="photo pain-photo p3" role="img" aria-label="Older woman pressing her jaw in pain"></div>
  <div class="photo pain-photo p4" role="img" aria-label="Woman holding her cheek with jaw pain"></div>
  <ul class="abs conditions bold">
    <li><svg width="22" height="20" viewBox="0 0 22 20"><rect x="1" y="5" width="14" height="14" fill="none" stroke="var(--purple)" stroke-width="2"/><path d="M4 11 L8 15 L20 2" fill="none" stroke="var(--blue)" stroke-width="3"/></svg>HEADACHES</li>
    <li><svg width="22" height="20" viewBox="0 0 22 20"><rect x="1" y="5" width="14" height="14" fill="none" stroke="var(--purple)" stroke-width="2"/><path d="M4 11 L8 15 L20 2" fill="none" stroke="var(--blue)" stroke-width="3"/></svg>MYOFASCIAL PAIN</li>
    <li><svg width="22" height="20" viewBox="0 0 22 20"><rect x="1" y="5" width="14" height="14" fill="none" stroke="var(--purple)" stroke-width="2"/><path d="M4 11 L8 15 L20 2" fill="none" stroke="var(--blue)" stroke-width="3"/></svg>NEUROPATHIC PAIN</li>
    <li><svg width="22" height="20" viewBox="0 0 22 20"><rect x="1" y="5" width="14" height="14" fill="none" stroke="var(--purple)" stroke-width="2"/><path d="M4 11 L8 15 L20 2" fill="none" stroke="var(--blue)" stroke-width="3"/></svg>TMJ</li>
    <li><svg width="22" height="20" viewBox="0 0 22 20"><rect x="1" y="5" width="14" height="14" fill="none" stroke="var(--purple)" stroke-width="2"/><path d="M4 11 L8 15 L20 2" fill="none" stroke="var(--blue)" stroke-width="3"/></svg>OBSTRUCTIVE SLEEP APNEA</li>
  </ul>
  <div class="abs web"><svg width="15" height="15" viewBox="0 0 12 12"><circle cx="6" cy="6" r="5" fill="none" stroke="#fff"/><path d="M1 6 H11 M6 1 V11" stroke="#fff"/></svg>www.BrightJPR.net</div>
</main>
</body>
</html>
```